Lou Benfield Tennis Academy - New Website

Our business is built around classes for all ages, competitions, and court hire.

There are a few gym style Wordpress templates that I think will have most of the functionality we need, but we don't like the style. We are looking for someone to make us a design that can be implemented as a child theme to one of these gym based Wordpress themes.

We have looked at:

http://stylebazaar.net/item/active-hall-responsive-wordpress-theme/full_screen_preview/7381926?ref=PixDepot
http://www.zulu-layouts.com/item/gym-fitness/demo/?r=pixdepot
http://www.pribo.tf/redirect/?theme=movenow

For style we are looking for something fresh, clean, and vibrant. Our logo is teal and gold with some red, orange, green and yellow.

https://huetray.examplehub.com/Mineral-D-color-theme-837465/
https://huetray.examplehub.com/Lozenge-D-color-theme-619372/
https://huetray.examplehub.com/Palermo-color-theme-57031/

These are the colour schemes we are leaning towards.

Our current website can be seen here www.lbta.com.au
Updates

The new logo design will be uploaded shortly. We don't need any more work done on that.

A rough logo file has been added for you to work with.

Could I please get some submissions that include what the other pages on the website will look like (instead of just the home page).

I think it's really important that we get the look of the product page. See the design pdf for our ideas on the layout of those pages.

***Edit*** Single product pages, I mean. I think the "Classes" page itself will be based a lot on the theme used so I'm less concerned about that. I just want to see what a page will look like that is only for.... Social Tennis (for example)

Target Market(s)

We teach a lot of kids but also many comp players. Everything needs to be very clear and easy to navigate.

Industry/Entity Type

Court

Requirements
Must have
• Custom content types to easily post new things (eg, new programs, new coaches)
Timetable page that is dynamic based on the programs custom type.
Programs page that is dynamic based on the programs custom type.
Coaches page that is dynamic based on the coaches/trainers content type.

Page templates for programs, competitions and a few other things as per pdf.

```html
<!DOCTYPE html>
<html lang="en">
<head>
<meta charset="utf-8">
<title>Lou Benfield Tennis Academy</title>
<link rel="stylesheet" href="https://fonts.googleapis.com/css2?family=Arimo:wght@400;700&family=Archivo+Black&family=Playfair+Display:wght@700&display=swap">
<style>
  :root{
    --topbar:#2b2b24;
    --rust:#8c2b0c;
    --teal:#41855f;
    --cream:#fdeba5;
    --orange:#fca93d;
    --orange-active:#eea043;
    --brick:#b94a2b;
    --banner:#9d3b22;
    --page:#f6f3ec;
    --rule:#dedad2;
    --text:#555;
    --ink:#222;
    --date:#3d7f9a;
    --white:#fff;
    --gold:#e7b325;
    --gold-dark:#a87a12;
    --feed:#f08a2c;
    --cal-red:#d42a2a;
  }
  *{box-sizing:border-box;margin:0;padding:0}
  html,body{width:1200px;height:675px;overflow:hidden}
  body{background:var(--page);font-family:"Arimo",Arial,sans-serif;color:var(--text);position:relative}
  .abs{position:absolute}

  .top-bar{left:0;top:0;width:1200px;height:14px;background:var(--topbar)}
  .social{left:773px;top:3px;display:flex;gap:2px}
  .social span{width:8px;height:8px;border-radius:50%;background:#8fb3c9;display:block}

  .bands{left:0;top:14px;width:1200px;height:221px;display:flex}
  .bands div{height:100%}
  .b1{width:150px;background:var(--rust)}
  .b2{width:180px;background:var(--teal)}
  .b3{width:180px;background:var(--cream)}
  .b4{width:180px;background:var(--orange)}
  .b5{width:180px;background:var(--brick)}
  .b6{width:180px;background:var(--rust)}
  .b7{width:150px;background:var(--teal)}

  .brand{left:378px;top:30px;display:flex;align-items:center;gap:4px}
  .brand-mark{width:9px;height:9px;background:var(--teal);flex:none}
  .brand-name{font-size:7.5px;font-weight:700;color:var(--teal);line-height:1.2}

  .nav-active{left:569px;top:14px;width:41px;height:47px;background:var(--orange-active)}
  .nav a{position:absolute;top:34px;font-size:6.5px;color:var(--ink);text-decoration:none;white-space:nowrap}
  .nav .caret::after{content:"▾";font-size:5px;margin-left:1px}
  .nav-rule{left:375px;top:61px;width:450px;height:1px;background:#5a4a3a}

  .slide-side{top:89px;width:98px;height:170px}
  .slide-left{left:375px;background:
    radial-gradient(circle at 40% 47%,#e8e84a 0 5px,transparent 6px),
    linear-gradient(155deg,#3f6230 0%,#2a4a22 38%,#e6e2dc 60%,#c9c3bb 100%)}
  .slide-right{left:727px;background:linear-gradient(160deg,#b35a35 0%,#c98a66 30%,#e2ddd8 58%,#8e9bb2 100%)}
  .slide-main{left:473px;top:80px;width:254px;height:188px;box-shadow:0 2px 6px rgba(0,0,0,.4);
    background:linear-gradient(180deg,#5f666f 0%,#c9ccd0 18%,#8c9198 34%,#3a3d40 46%,#54585c 62%,#6b655e 100%)}
  .caption{left:473px;top:209px;width:254px;height:59px;background:rgba(20,20,20,.38);color:var(--white);padding:12px 10px 0}
  .caption h3{font-size:7px;font-weight:700;margin-bottom:7px}
  .caption p{font-size:5.3px;line-height:9.5px}
  .arrow{top:167px;width:14px;height:14px;border-radius:50%;background:#c8c4b8}
  .arrow svg{display:block}
  .arrow-prev{left:354px}
  .arrow-next{left:832px;background:#3a2a22}

  .promo{left:375px;top:289px;width:450px;height:93px;display:flex}
  .promo-photo{width:253px;height:100%;background:
    linear-gradient(180deg,#5e6e4a 0 9%,transparent 14%),
    linear-gradient(90deg,#b8573a 0%,#d9c2b0 18%,#e8d2bf 34%,#c4cad8 48%,#b4583a 62%,#a54a2f 100%)}
  .promo-text{flex:1;background:var(--banner);color:var(--white);position:relative;padding:21px 0 0 12px}
  .promo-text h2{font-family:"Archivo Black",Arial,sans-serif;font-size:18.5px;line-height:17px;letter-spacing:.3px;font-weight:400}
  .promo-text .more{position:absolute;left:138px;top:64px;font-size:7px;font-weight:700;color:#e8d3c8}

  .rule{left:375px;width:450px;height:1px;background:var(--rule)}

  .section-title{left:375px;top:401px;display:flex;align-items:center;gap:3px}
  .section-icon{width:20px;height:16px;background:linear-gradient(135deg,#666 0 45%,#999 55%);border-radius:3px}
  .section-title h2{font-family:"Playfair Display",Georgia,serif;font-size:15px;color:var(--ink);letter-spacing:-.3px;transform:scaleX(.76);transform-origin:left center}

  .post{top:434px;width:114px;display:flex;gap:10px}
  .post-thumb{width:23px;height:23px;flex:none;background:#c9ced4}
  .post-thumb.photo{background:linear-gradient(135deg,#2f3f5e,#8d9aab)}
  .post h4{font-size:6.3px;font-weight:400;color:var(--text);line-height:1.55;white-space:normal}
  .post time{font-size:4.6px;font-weight:700;color:var(--date);display:block;margin-top:3px}

  .feature{text-align:center;font-size:6px;color:var(--text);text-transform:uppercase}
  .feature svg{display:block;margin:0 auto 7px}
</style>
</head>
<body>
  <div class="abs top-bar"></div>
  <div class="abs social" aria-label="Social links">
    <span></span><span></span><span></span><span></span><span></span>
  </div>

  <div class="abs bands">
    <div class="b1"></div><div class="b2"></div><div class="b3"></div><div class="b4"></div><div class="b5"></div><div class="b6"></div><div class="b7"></div>
  </div>

  <div class="abs brand">
    <span class="brand-mark"></span>
    <span class="brand-name">Lou Benfield<br>Tennis Academy</span>
  </div>

  <div class="abs nav-active"></div>
  <nav class="nav">
    <a href="#" style="left:576px">Homepage</a>
    <a class="caret" href="#" style="left:618px">About</a>
    <a class="caret" href="#" style="left:648px">Program Page</a>
    <a class="caret" href="#" style="left:701px">Services</a>
    <a class="caret" href="#" style="left:744px">Competitions Page</a>
    <a href="#" style="left:805px">Blog</a>
  </nav>
  <div class="abs nav-rule"></div>

  <div class="abs slide-side slide-left" role="img" aria-label="Young player hitting a tennis ball on a green court"></div>
  <div class="abs slide-side slide-right" role="img" aria-label="Young boy in a tracksuit on a clay court"></div>
  <div class="abs slide-main" role="img" aria-label="Two tennis players sitting on the net with rackets under a cloudy sky"></div>
  <div class="abs caption">
    <h3>What We Do</h3>
    <p>Amet est ut integer non orci. Ipsum enim convallis. Vero dolor praesent. Vivamus luctus nulla in pellentesque odio. Justo vestibulum phasellus at mollis consectetuer. Sem adipiscing wisi. Et in nulla. Lorem hendrerit mattis. Nisi nec ut.</p>
  </div>
  <div class="abs arrow arrow-prev"><svg width="14" height="14" viewBox="0 0 14 14"><path d="M8 4 5 7l3 3" fill="none" stroke="#333" stroke-width="1.5"/></svg></div>
  <div class="abs arrow arrow-next"><svg width="14" height="14" viewBox="0 0 14 14"><path d="M6 4l3 3-3 3" fill="none" stroke="#fff" stroke-width="1.5"/></svg></div>

  <section class="abs promo">
    <div class="promo-photo" role="img" aria-label="Smiling toddler holding a tennis racket on a clay court"></div>
    <div class="promo-text">
      <h2>EARLY<br>DEVELOPMENT<br>CLASS</h2>
      <span class="more">&gt;&gt;more</span>
    </div>
  </section>

  <div class="abs rule" style="top:389px"></div>

  <div class="abs section-title">
    <div class="section-icon" role="img" aria-label="Crossed tennis rackets ornament"></div>
    <h2>Attention Grabber</h2>
  </div>

  <article class="abs post" style="left:375px">
    <div class="post-thumb photo" role="img" aria-label="Post thumbnail"></div>
    <div><h4>FLC Schedule June 21</h4><time>September 9, 2013</time></div>
  </article>
  <article class="abs post" style="left:489px">
    <div class="post-thumb" role="img" aria-label="Post thumbnail placeholder"></div>
    <div><h4>Tournament Tough cancelled. New camp next week.</h4><time>September 9, 2013</time></div>
  </article>
  <article class="abs post" style="left:604px">
    <div class="post-thumb" style="background:#e6e6e2" role="img" aria-label="Hoodie sketch thumbnail"></div>
    <div><h4>Holler for a Hoodie Winners</h4><time>September 9, 2013</time></div>
  </article>
  <article class="abs post" style="left:719px">
    <div class="post-thumb" role="img" aria-label="Post thumbnail placeholder"></div>
    <div><h4>Rain Make Ups Term 3-2013</h4><time>September 9, 2013</time></div>
  </article>

  <div class="abs rule" style="top:477px"></div>

  <div class="abs feature" style="left:391px;top:504px;width:104px">
    <svg width="44" height="62" viewBox="0 0 44 62" role="img" aria-label="Gold trophy">
      <path d="M9 8H3c0 10 5 16 10 17M35 8h6c0 10-5 16-10 17" fill="none" stroke="var(--gold-dark)" stroke-width="2.5"/>
      <path d="M8 2h28v10c0 11-6 18-14 18S8 23 8 12z" fill="var(--gold)"/>
      <path d="M13 4h4v10c0 6 2 10 5 12-5-1-9-6-9-12z" fill="#f7dc74"/>
      <rect x="19" y="30" width="6" height="10" fill="var(--gold-dark)"/>
      <rect x="13" y="40" width="18" height="4" rx="1" fill="var(--gold)"/>
      <rect x="9" y="44" width="26" height="17" rx="2" fill="#2a2a2a"/>
      <rect x="9" y="44" width="26" height="4" fill="#555"/>
    </svg>
    Player of the month
  </div>
  <div class="abs feature" style="left:550px;top:516px;width:100px">
    <svg width="44" height="45" viewBox="0 0 44 45" role="img" aria-label="Orange feed icon">
      <rect x="1" y="1" width="42" height="42" rx="6" fill="var(--feed)" stroke="#c85f18" stroke-width="1.5"/>
      <circle cx="13" cy="31" r="4" fill="#fff"/>
      <path d="M9 19a15 15 0 0 1 15 15M9 9a25 25 0 0 1 25 25" fill="none" stroke="#fff" stroke-width="5" stroke-linecap="round"/>
    </svg>
    Recent post
  </div>
  <div class="abs feature" style="left:706px;top:510px;width:100px">
    <svg width="44" height="48" viewBox="0 0 44 48" role="img" aria-label="Calendar showing upcoming date 25">
      <rect x="0" y="0" width="44" height="47" fill="#fafafa" stroke="#ddd"/>
      <rect x="0" y="0" width="44" height="11" fill="var(--cal-red)"/>
      <text x="22" y="8.3" text-anchor="middle" font-family="Arimo, Arial, sans-serif" font-size="6.5" font-weight="700" fill="#fff">UPCOMING</text>
      <text x="22" y="36" text-anchor="middle" font-family="Arimo, Arial, sans-serif" font-size="22" font-weight="700" fill="#111">25</text>
    </svg>
    Upcoming events
  </div>
</body>
</html>
```